Business Cards for a Junk Removal Company

Hello,
We are looking to have business cards designed that are simple, bold, easy to read, and right to the point. Please see the attachments for our logo files. We want the card to be yellow on both sides ( Color code Yellow: #FFE01B). The logo text font is (Rockstar Extra Bold) and this is also in the files attached. Please make the text black for the logo. On the back side of the card, you can use white and black for text. Thank you in advance for your hard work!

Front of card-
Harbor Haul Away (logo)
Back of card-
Harbor Haul Away
Donate - Recycle - Dispose
555-271-8093
www.harborhaulaway.example
info@harborhaulaway.example

Industry/Entity Type

Junk removal

Contact Information for Business Card

FRONT OF CARD- Harbor Haul Away (logo) BACK OF CARD- Harbor Haul Away Donate - Recycle - Dispose 555-271-8093 www.harborhaulaway.example info@harborhaulaway.example

Font styles to use
Other font styles liked:
• Rockstar Extra Bold

Colors
FFF300
FFF600
FEFA6F
FFFEC7
FFFEE8

Requirements
Must have
• Must have color code Yellow: #FFE01B for the background of front and back of the card

```html
<!DOCTYPE html>
<html lang="en">
<head>
<meta charset="utf-8">
<title>Harbor Haul Away – Business Cards</title>
<link rel="stylesheet" href="https://fonts.googleapis.com/css2?family=Barlow+Condensed:wght@800&display=swap">
<style>
  :root {
    --stage: #262626;
    --card-yellow: #ECD349;
    --ink: #000000;
    --card-radius: 30px;
  }
  * { margin: 0; padding: 0; box-sizing: border-box; }
  html, body {
    width: 1200px;
    height: 1200px;
    overflow: hidden;
    background: var(--stage);
  }
  .canvas {
    position: relative;
    width: 1200px;
    height: 1200px;
    font-family: "Barlow Condensed", "Arial Narrow", sans-serif;
    font-weight: 800;
    color: var(--ink);
  }
  .card {
    position: absolute;
    width: 700px;
    height: 398px;
    background: var(--card-yellow);
    border-radius: var(--card-radius);
    text-align: center;
  }
  .card--front { left: 246px; top: 175px; }
  .card--back  { left: 239px; top: 627px; }

  /* Front: company name in the card's text face */
  .front-name {
    position: absolute;
    left: 0; right: 0;
    font-size: 120px;
    line-height: 1;
    letter-spacing: 6px;
    text-transform: uppercase;
  }
  .front-name--top { top: 81px; }
  .front-name--bottom { top: 193px; }

  /* Back: contact details */
  .back-line {
    position: absolute;
    left: 0; right: 0;
    line-height: 1;
    text-transform: uppercase;
  }
  .company-name { top: 79px; font-size: 53px; letter-spacing: 2px; }
  .services { top: 137px; font-size: 29px; letter-spacing: 1px; }
  .phone-bar {
    position: absolute;
    left: 89px;
    top: 179px;
    width: 522px;
    height: 70px;
    background: var(--ink);
    color: var(--card-yellow);
    font-size: 84px;
    line-height: 72px;
    letter-spacing: 4px;
  }
  .email { top: 261px; font-size: 31px; }
  .website { top: 297px; font-size: 31px; }
</style>
</head>
<body>
  <main class="canvas">
    <section class="card card--front" aria-label="Card front">
      <p class="front-name front-name--top">Harbor</p>
      <p class="front-name front-name--bottom">Haul Away</p>
    </section>

    <section class="card card--back" aria-label="Card back">
      <h1 class="back-line company-name">Harbor Haul Away</h1>
      <p class="back-line services">Donate - Recycle - Dispose</p>
      <p class="phone-bar">555-271-8093</p>
      <p class="back-line email">info@harborhaulaway.example</p>
      <p class="back-line website">www.harborhaulaway.example</p>
    </section>
  </main>
</body>
</html>
```